Web Design Project for Wren Nectar

We are a Honey Packing Company called Wren Nectar.
We need a new website.
We are open to many ideas.
We want to have headings like: Home/Products/About Us/Contact Us
We want an easy and uncomplicated website.
We need our logo attached to the center top or left top of the webpage.
We want to have a number of our products on the first page that increase in size once the cursor is placed on them.
We want to be able to add photos and products in the future as we expand.
Updates
Target Market(s)
Public
Food Distributors
Importers/Exporters
Industry/Entity Type
It Company
Look and feel
Each slider illustrates characteristics of the customer's brand and the style your logo design should communicate.

```html
<!DOCTYPE html>
<html lang="en">
<head>
<meta charset="utf-8">
<title>Wren Nectar – Australia's 100% Pure Honey</title>
<link rel="stylesheet" href="https://fonts.googleapis.com/css2?family=Source+Sans+3:wght@400;600;700;800&display=swap">
<style>
:root{
  --honey-deep:#b8561a;
  --honey-mid:#e39a45;
  --honey-light:#f6d6ae;
  --cream:#fbeee0;
  --nav-top:#c9b7a0;
  --nav-bottom:#8d7760;
  --ink:#111111;
  --title-gold:#e39416;
  --product-red:#c8342c;
  --footer-brown:#4b1d12;
  --footer-text:#e9d9cf;
  --button-red:#8a2318;
  --rim-gold:#d8b25a;
  --white:#ffffff;
}
*{box-sizing:border-box;margin:0;padding:0}
html,body{width:1092px;height:1200px;overflow:hidden;background:var(--white)}
body{position:relative;font-family:"Source Sans 3",Arial,sans-serif;color:var(--ink)}

.hero{position:absolute;left:0;top:0;width:1092px;height:376px;
  background:
    radial-gradient(ellipse 420px 300px at 240px 160px,rgba(255,240,220,.55),transparent 70%),
    radial-gradient(ellipse 380px 260px at 950px 120px,rgba(255,255,255,.85),transparent 70%),
    linear-gradient(160deg,var(--honey-deep) 0%,var(--honey-mid) 35%,var(--honey-light) 70%,var(--cream) 100%);}
.scallop{position:absolute;left:0;width:1092px;height:16px}
.hero-scallop{top:368px}

.main-nav{position:absolute;left:184px;top:48px;width:724px;height:34px;
  background:linear-gradient(var(--nav-top),var(--nav-bottom));border-radius:3px;
  box-shadow:0 2px 4px rgba(0,0,0,.35)}
.main-nav a{position:absolute;top:6px;font-size:15px;font-weight:700;color:var(--ink);text-decoration:none}
.nav-home{left:56px}.nav-products{left:170px}.nav-about{left:496px}.nav-contact{left:618px;color:var(--white)!important}
.brand{position:absolute;left:471px;top:41px;width:150px;height:116px;display:flex;align-items:center;justify-content:center;
  font-size:25px;font-weight:800;color:var(--footer-brown);text-align:center;line-height:1}

.hero-title{position:absolute;left:200px;top:140px;font-weight:800;line-height:1}
.hero-title .line1{display:block;font-size:47px;letter-spacing:-.5px}
.hero-title .line2{display:block;font-size:34px;margin-top:6px}
.hero-rule{position:absolute;left:202px;top:248px;width:330px;height:1px;background:rgba(80,30,10,.35)}
.hero-copy{position:absolute;left:202px;top:256px;width:345px;font-size:12px;line-height:14px}
.order-btn{position:absolute;left:407px;top:303px;width:132px;height:31px;border-radius:16px;
  background:linear-gradient(#a8352a,var(--button-red));color:var(--white);font-size:12px;font-weight:700;
  display:flex;align-items:center;padding-left:28px;gap:13px;box-shadow:0 2px 3px rgba(0,0,0,.3)}
.order-btn svg{width:19px;height:19px}
.hero-bottles{position:absolute;left:607px;top:157px;width:301px;height:184px;border-radius:12px;
  background:linear-gradient(90deg,#c96a12,#e6a235 50%,#c96a12)}

.products{position:absolute;left:182px;top:400px;width:730px;height:613px;background:var(--white);
  box-shadow:0 0 8px rgba(0,0,0,.25)}
.products h2{position:absolute;left:0;right:0;top:12px;text-align:center;font-size:27px;font-weight:800;
  color:var(--title-gold);text-shadow:1px 1px 1px rgba(90,40,0,.45)}
.product{position:absolute;width:170px;text-align:center}
.product-photo{width:147px;height:147px;margin:0 auto;border-radius:50%;border:2px solid var(--rim-gold);
  background:radial-gradient(circle at 50% 55%,#e08a1c 0 30%,#9a9aa0 55%,#7c7c84 100%);
  box-shadow:0 2px 4px rgba(0,0,0,.3)}
.product h3{margin-top:13px;font-size:17px;font-weight:400;color:var(--product-red)}
.product p{margin-top:4px;font-size:12px;line-height:14px}
.c1{left:18px}.c2{left:196px}.c3{left:372px}.c4{left:547px}
.r1{top:76px}.r2{top:341px}

.site-footer{position:absolute;left:0;top:1013px;width:1092px;height:187px;background:var(--footer-brown);color:var(--footer-text)}
.footer-scallop{top:-8px}
.news{position:absolute;left:184px;top:25px;width:225px}
.news h4{font-size:13px;font-weight:700;color:var(--white);padding-bottom:9px;border-bottom:1px solid rgba(255,255,255,.15)}
.news time{display:block;margin-top:6px;font-size:10px;font-weight:700}
.news p{margin-top:12px;font-size:10px;line-height:12px;font-weight:600}
.news a{display:inline-block;margin-top:6px;font-size:10px;font-weight:700;color:var(--footer-text);border-bottom:1px solid var(--footer-text)}
.newsletter{position:absolute;left:432px;top:24px;width:230px;text-align:center}
.newsletter h4{display:flex;align-items:center;justify-content:flex-start;gap:6px;font-size:17px;font-weight:700;color:var(--white);margin-left:9px}
.newsletter h4 svg{width:30px;height:30px}
.newsletter p{margin-top:6px;font-size:11px;font-weight:700}
.field{background:var(--white);color:#444;font-size:10px;padding:3px 6px}
.newsletter .field{margin-top:9px;height:19px;border-radius:10px;text-align:left;width:228px}
.btn-light{display:inline-block;background:var(--white);color:var(--ink);font-size:11px;font-weight:600;padding:2px 14px;margin-top:8px}
.contact-form{position:absolute;left:696px;top:24px;width:214px}
.contact-form .field{height:20px;margin-bottom:4px}
.contact-form .message{height:54px}
.form-actions{position:absolute;left:48px;top:108px;display:flex;gap:14px}
.form-actions span{display:block;width:56px;height:18px;border-radius:4px;background:var(--white);font-size:10px;font-weight:700;text-align:center;line-height:18px}
.form-actions .submit{color:var(--product-red)}
.copyright{position:absolute;left:0;right:0;top:166px;text-align:center;font-size:11px}
</style>
</head>
<body>
<svg width="0" height="0" style="position:absolute">
  <defs>
    <pattern id="scallop-white" width="16" height="16" patternUnits="userSpaceOnUse"><circle cx="8" cy="16" r="8" fill="#ffffff"/></pattern>
    <pattern id="scallop-brown" width="16" height="16" patternUnits="userSpaceOnUse"><circle cx="8" cy="8" r="8" fill="#4b1d12"/></pattern>
  </defs>
</svg>

<header class="hero">
  <div class="hero-photo" role="img" aria-label="Close-up of golden honey flowing in a glass jar" style="position:absolute;inset:0"></div>
  <nav class="main-nav">
    <a class="nav-home">Home</a>
    <a class="nav-products">Products</a>
    <a class="nav-about">About Us</a>
    <a class="nav-contact">Contact Us</a>
  </nav>
  <div class="brand">Wren Nectar</div>
  <h1 class="hero-title"><span class="line1">Australia’s</span><span class="line2">100% Pure Honey</span></h1>
  <div class="hero-rule"></div>
  <p class="hero-copy">Lorem Ipsum is simply dummy text of the printing and typesetting industry. Lorem Ipsum has been the industry's standard dummy text ever since the 1500s.</p>
  <div class="order-btn">ORDER NOW
    <svg viewBox="0 0 20 20"><circle cx="10" cy="10" r="10" fill="#fff"/><path d="M8 5l5 5-5 5" stroke="#8a2318" stroke-width="2.4" fill="none"/></svg>
  </div>
  <div class="hero-bottles" role="img" aria-label="Three squeeze bottles of pure honey in different sizes"></div>
  <svg class="scallop hero-scallop"><rect width="1092" height="16" fill="url(#scallop-white)"/></svg>
</header>

<section class="products">
  <h2>Range of Our Products</h2>
  <div class="product c1 r1"><div class="product-photo" role="img" aria-label="Honey jar with yellow lid"></div><h3>Lorem Ipsum</h3><p>is simply dummy text<br>of the printing and<br>typesetting industry.</p></div>
  <div class="product c2 r1"><div class="product-photo" role="img" aria-label="Honey squeeze bottle"></div><h3>Lorem Ipsum</h3><p>is simply dummy text<br>of the printing and<br>typesetting industry.</p></div>
  <div class="product c3 r1"><div class="product-photo" role="img" aria-label="Honey bucket with handle"></div><h3>Lorem Ipsum</h3><p>is simply dummy text<br>of the printing and<br>typesetting industry.</p></div>
  <div class="product c4 r1"><div class="product-photo" role="img" aria-label="Honey jar with yellow lid"></div><h3>Lorem Ipsum</h3><p>is simply dummy text<br>of the printing and<br>typesetting industry.</p></div>
  <div class="product c1 r2"><div class="product-photo" role="img" aria-label="Honey jar with yellow lid"></div><h3>Lorem Ipsum</h3><p>is simply dummy text<br>of the printing and<br>typesetting industry.</p></div>
  <div class="product c2 r2"><div class="product-photo" role="img" aria-label="Honey squeeze bottle"></div><h3>Lorem Ipsum</h3><p>is simply dummy text<br>of the printing and<br>typesetting industry.</p></div>
  <div class="product c3 r2"><div class="product-photo" role="img" aria-label="Honey bucket with handle"></div><h3>Lorem Ipsum</h3><p>is simply dummy text<br>of the printing and<br>typesetting industry.</p></div>
  <div class="product c4 r2"><div class="product-photo" role="img" aria-label="Honey jar with yellow lid"></div><h3>Lorem Ipsum</h3><p>is simply dummy text<br>of the printing and<br>typesetting industry.</p></div>
</section>

<footer class="site-footer">
  <svg class="scallop footer-scallop"><rect width="1092" height="16" fill="url(#scallop-brown)"/></svg>
  <div class="news">
    <h4>Latest News:</h4>
    <time>24-09-2011</time>
    <p>Lorem Ipsum is simply dummy text of the printing and typesetting industry. Lorem Ipsum has been the industry's standard dummy text ever since the 1500s, when an unknown printer took a galley of type and scrambled it to make a type specimen book.</p>
    <a>+ VIEW ALL</a>
  </div>
  <div class="newsletter">
    <h4><svg viewBox="0 0 30 30"><circle cx="15" cy="15" r="14" fill="#3a78c8" stroke="#fff" stroke-width="1.5"/><rect x="7" y="10" width="16" height="11" fill="#fff"/><path d="M7 10l8 6 8-6" stroke="#3a78c8" stroke-width="1.4" fill="none"/></svg>Newsletter Signup</h4>
    <p>Subscribe Now and Get Lattest Updates...</p>
    <div class="field">Enter Email Address...</div>
    <span class="btn-light">Subscribe Now</span>
  </div>
  <div class="contact-form">
    <div class="field">Name...</div>
    <div class="field">Email...</div>
    <div class="field message">Message...</div>
    <div class="form-actions"><span class="submit">Submit</span><span>Clear</span></div>
  </div>
  <p class="copyright">Copyright©2011 P | All Wren Nectar Australia, All Rights Reserved.</p>
</footer>
</body>
</html>
```